Qolvar Energy Information Site Redesign

Re-vamp current site at qolvarenergy.com to include new logo, verbiage updates as needed, redesign, etc. Company overview and additional information on current QVR url.

```html
<!DOCTYPE html>
<html lang="en">
<head>
<meta charset="utf-8">
<title>Qolvar Energy Information</title>
<link rel="stylesheet" href="https://fonts.googleapis.com/css2?family=Open+Sans:wght@400;600;700&display=swap">
<style>
:root{
  --blue:#1b74c4;
  --blue-dark:#0f4f8f;
  --orange:#f7931e;
  --ink:#333;
  --muted:#8a8a8a;
  --line:#e3e3e3;
  --gray-bg:#f3f3f3;
  --black:#0b0b0b;
  --white:#fff;
}
*{box-sizing:border-box;margin:0;padding:0}
html,body{width:1200px;height:5012px;overflow:hidden}
body{font-family:"Open Sans",Arial,sans-serif;color:var(--ink);background:var(--white);position:relative}
section,header,footer{position:relative;width:1200px;overflow:hidden}

/* header */
.site-header{height:140px;display:flex;align-items:center;padding:0 40px}
.brand{display:flex;align-items:center;gap:10px;width:250px}
.brand-mark{width:34px;height:34px;border-radius:50%;background:var(--orange)}
.brand-name{font-size:24px;font-weight:700;color:var(--blue);letter-spacing:.5px}
.main-nav{display:flex;gap:34px;font-size:15px;margin-left:50px}
.main-nav a{color:var(--ink);text-decoration:none;padding-bottom:6px}
.main-nav a.active{color:var(--blue);border-bottom:2px solid var(--blue)}
.header-contact{margin-left:auto;display:flex;align-items:center;gap:10px;font-size:20px;font-weight:600;color:var(--blue-dark)}
.header-contact svg{width:26px;height:26px}
.social{display:flex;gap:8px;margin-left:18px}
.social span{width:12px;height:12px;border-radius:50%;background:var(--blue)}

/* hero */
.hero{height:500px;background:linear-gradient(120deg,#0b3f8a 0%,#2a7fd6 45%,#9cc9f2 75%,#2f6fc0 100%);display:flex;flex-direction:column;align-items:center;justify-content:center;color:var(--white)}
.hero h1{font-size:38px;font-weight:400;text-align:center;line-height:1.35;max-width:960px;margin-top:-80px}
.hero-dots{position:absolute;bottom:54px;display:flex;gap:10px}
.hero-dots span{width:10px;height:10px;border-radius:50%;background:rgba(255,255,255,.5)}
.hero-dots span:first-child{background:var(--white)}

.section-title{display:flex;align-items:center;justify-content:center;gap:12px;font-size:30px;font-weight:400;color:var(--blue-dark)}
.section-title i{width:22px;height:22px;border:3px solid var(--blue);border-radius:50%}

.btn{display:inline-block;background:var(--blue);color:var(--white);font-size:13px;padding:9px 24px;border-radius:2px}

/* about */
.about{height:520px;padding-top:74px}
.about-body{display:flex;gap:60px;margin:70px 0 0 192px}
.about-image{width:368px;height:204px;background:linear-gradient(135deg,#1c1c1c,#4a4a4a 50%,#1a1a1a)}
.about-text{width:440px;font-size:14px;line-height:1.75;color:#555}
.about-text .btn{margin-top:18px}

.photo-band{height:460px}
.photo-oil{background:linear-gradient(180deg,#3a2a1c 0%,#b85d1a 45%,#f3a93a 70%,#2a1a10 100%)}
.photo-map{height:580px;background:linear-gradient(120deg,#e6edf5 0%,#9fb9d6 40%,#5b86b8 70%,#cfd9e6 100%)}

/* clients */
.clients{height:540px;background:var(--gray-bg);padding-top:100px}
.client-grid{display:grid;grid-template-columns:repeat(9,1fr);width:940px;margin:52px auto 0;row-gap:9px;font-size:12px;color:#666}
.client-grid li{list-style:none;display:flex;align-items:center;gap:8px}
.client-grid li::before{content:"";width:5px;height:5px;background:var(--blue)}

/* services */
.services{height:580px;padding-top:84px;text-align:center}
.service-cards{display:flex;gap:22px;justify-content:center;margin-top:76px}
.service-card{width:182px;height:192px;border:1px solid var(--line);box-shadow:0 2px 6px rgba(0,0,0,.06);padding:22px 14px}
.service-card svg{width:22px;height:22px}
.service-card h3{font-size:13px;font-weight:600;color:var(--blue-dark);margin:8px 0 12px;line-height:1.3}
.service-card p{font-size:11px;line-height:1.6;color:var(--muted)}
.services .btn{margin-top:78px}

/* contact */
.contact{height:540px;background:var(--blue);color:var(--white);text-align:center;padding-top:56px}
.contact h2{font-size:28px;font-weight:600;line-height:1.35}
.contact .lead{font-size:16px;font-weight:600;margin-top:30px}
.contact .small{font-size:12px;width:440px;margin:12px auto 0;line-height:1.5}
.contact-form{width:660px;margin:26px auto 0;display:flex;flex-wrap:wrap;gap:14px}
.field{flex:1;height:34px;background:var(--white);color:#999;font-size:12px;text-align:left;padding:8px 10px}
.field.message{flex-basis:100%;height:88px}
.send{background:var(--orange);color:var(--white);font-size:13px;font-weight:600;padding:9px 46px;margin:18px auto 0}

/* blog */
.blog{height:580px;padding-top:140px}
.blog-row{display:flex;gap:28px;justify-content:center;margin-top:52px;position:relative}
.blog-card{width:300px;height:268px;border:1px solid var(--line);box-shadow:0 2px 6px rgba(0,0,0,.06)}
.blog-image{height:124px;background:linear-gradient(135deg,#0b3f8a,#3a8ee0 60%,#f39a2e)}
.blog-card:nth-child(2) .blog-image{background:linear-gradient(135deg,#cfcfcf,#8d8d8d 60%,#efefef)}
.blog-card:nth-child(3) .blog-image{background:linear-gradient(180deg,#2a1a10,#c8641e 55%,#f5b34a)}
.blog-content{padding:12px 14px}
.blog-content h3{font-size:14px;font-weight:700;color:var(--blue-dark);line-height:1.35}
.blog-content time{display:block;font-size:10px;color:var(--muted);margin:4px 0 6px}
.blog-content p{font-size:10px;color:var(--muted);line-height:1.5}
.blog-content a{display:block;font-size:11px;color:var(--blue);margin-top:8px;text-decoration:none}
.slider-arrow{position:absolute;top:120px;width:18px;height:30px}
.slider-arrow.prev{left:56px}.slider-arrow.next{right:56px}

/* newsletter */
.newsletter{height:80px;background:var(--orange);display:flex;align-items:center;padding-left:110px;gap:16px;color:var(--white)}
.newsletter svg{width:30px;height:30px}
.newsletter h2{font-size:24px;font-weight:400;width:300px}
.newsletter .field{flex:none;width:400px;height:32px}
.subscribe{background:#222;color:var(--white);font-size:12px;font-weight:600;padding:8px 30px;margin-left:-16px}

/* footer */
.site-footer{height:540px;background:var(--black);color:#ccc;display:flex;padding:56px 0 0 70px;gap:0}
.footer-brand{width:270px}
.footer-brand .brand{margin-bottom:24px}
.footer-brand p{font-size:12px;line-height:1.6;width:200px}
.footer-col{width:230px;font-size:12px;line-height:1.9}
.footer-col h4{color:var(--white);font-size:14px;font-weight:600;margin-bottom:10px}
.footer-col .item{display:flex;gap:10px;margin-bottom:14px}
.footer-col .item svg{flex:none;width:16px;height:16px;margin-top:3px}
.touch-form{display:flex;flex-wrap:wrap;gap:8px;width:240px}
.touch-form .field{flex:1 1 100px;height:26px;font-size:11px;padding:4px 8px}
.touch-form .field.full{flex-basis:100%}
.touch-form .send{margin:4px 0 0;padding:6px 26px;font-size:12px}
.copyright{height:32px;background:#1d1d1d;color:#888;font-size:11px;display:flex;align-items:center;justify-content:center}
</style>
</head>
<body>

<header class="site-header">
  <div class="brand"><span class="brand-mark"></span><span class="brand-name">QOLVAR ENERGY</span></div>
  <nav class="main-nav">
    <a class="active">What We Do</a><a>Exchange Solutions</a><a>Data Management</a><a>Owner Relations Services</a><a>About QVR</a><a>Blog</a>
  </nav>
  <div class="header-contact">
    <svg viewBox="0 0 26 26"><circle cx="13" cy="13" r="13" fill="#1b74c4"/><path d="M9 7l3 3-2 2c1 2 2 3 4 4l2-2 3 3-2 2c-5 0-10-5-10-10z" fill="#fff"/></svg>
    1-888-555-0142
    <div class="social"><span></span><span></span><span></span></div>
  </div>
</header>

<section class="hero">
  <h1>QVR provides the technology to efficiently transfer information electronically and access, integrate and manage data.</h1>
  <div class="hero-dots"><span></span><span></span><span></span></div>
</section>

<section class="about">
  <h2 class="section-title"><i></i>About Us</h2>
  <div class="about-body">
    <div class="about-image" role="img" aria-label="Financial data charts on a dark screen"></div>
    <div class="about-text">
      <p>Qolvar Energy Information has been providing electronic exchange solutions for the energy industry for over 30 years. QVR utilizes secure data integration techniques to provide customers with cost effective methods to efficiently transfer, transform and distribute their data. Our customer list includes over 80% of the Fortune 500 energy companies.</p>
      <span class="btn">Read More</span>
    </div>
  </div>
</section>

<section class="photo-band photo-oil" role="img" aria-label="Oil pump jacks silhouetted against a sunset sky"></section>

<section class="clients">
  <h2 class="section-title"><i></i>Our Clients</h2>
  <ul class="client-grid">
    <li>Abernex</li><li>Galvera</li><li>Oakmere</li><li>Westrin</li><li>Falkner</li><li>Newell</li><li>Vance</li><li>Fairley</li><li>Nash</li>
    <li>Aldris</li><li>Harlow</li><li>Pelham</li><li>Yarrow</li><li>Glenrow</li><li>Orrin</li><li>Whitby</li><li>Grafton</li><li>Orwell</li>
    <li>Bramwell</li><li>Ironvale</li><li>Quorra</li><li>Zenmark</li><li>Hadley</li><li>Paxton</li><li>Yelton</li><li>Hollis</li><li>Prescott</li>
    <li>Calton</li><li>Jastro</li><li>Redvale</li><li>Ashby</li><li>Ingram</li><li>Quillan</li><li>Alder</li><li>Islay</li><li>Radford</li>
    <li>Corvane</li><li>Kelmont</li><li>Sandell</li><li>Brixton</li><li>Juniper</li><li>Ridley</li><li>Birch</li><li>Jarrow</li><li>Stanton</li>
    <li>Dalrick</li><li>Larkin</li><li>Tarrow</li><li>Carmel</li><li>Kestrel</li><li>Selwyn</li><li>Corwin</li><li>Kirby</li><li>Tilden</li>
    <li>Elstow</li><li>Merrow</li><li>Umbrel</li><li>Denholm</li><li>Lowell</li><li>Thorne</li><li>Drayton</li><li>Lyndon</li><li>Walcott</li>
    <li>Fenwick</li><li>Norcliff</li><li>Varnell</li><li>Elmira</li><li>Marden</li><li>Upton</li><li>Easton</li><li>Morley</li><li>Wexley</li>
  </ul>
</section>

<section class="services">
  <h2 class="section-title"><i></i>How can Help you!</h2>
  <div class="service-cards">
    <article class="service-card">
      <svg viewBox="0 0 22 22"><rect x="4" y="3" width="14" height="16" rx="2" fill="none" stroke="#1b74c4" stroke-width="2"/></svg>
      <h3>Data Management Solutions</h3>
      <p>Our data management solutions help you collect, validate and store records in one secure place.</p>
    </article>
    <article class="service-card">
      <svg viewBox="0 0 22 22"><path d="M3 8h14l-3-3M19 14H5l3 3" fill="none" stroke="#1b74c4" stroke-width="2"/></svg>
      <h3>Well Data Exchange</h3>
      <p>Exchange well and production data with partners quickly using standard formats and automated secure delivery.</p>
    </article>
    <article class="service-card">
      <svg viewBox="0 0 22 22"><circle cx="11" cy="11" r="8" fill="none" stroke="#1b74c4" stroke-width="2"/></svg>
      <h3>Partner Data Exchange</h3>
      <p>Share joint interest billing and revenue data with partners through one reliable and audited channel.</p>
    </article>
    <article class="service-card">
      <svg viewBox="0 0 22 22"><circle cx="5" cy="11" r="2.5" fill="#1b74c4"/><circle cx="17" cy="5" r="2.5" fill="#1b74c4"/><circle cx="17" cy="17" r="2.5" fill="#1b74c4"/><path d="M5 11L17 5M5 11l12 6" stroke="#1b74c4" stroke-width="1.6"/></svg>
      <h3>E-Ticket Exchange</h3>
      <p>Replace paper field tickets with electronic tickets that move from the field to accounting fast.</p>
    </article>
    <article class="service-card">
      <svg viewBox="0 0 22 22"><path d="M4 12l5 5 9-11" fill="none" stroke="#1b74c4" stroke-width="2"/></svg>
      <h3>Owner Relations Services</h3>
      <p>Give royalty owners clear statements, online access and prompt answers to questions about their payments.</p>
    </article>
  </div>
  <span class="btn">Read More</span>
</section>

<section class="contact">
  <h2>For more information on our services please<br>feel free to contact us.</h2>
  <p class="lead">If you have a project you would like to discuss, get in touch with us.</p>
  <p class="small">Let us know how we can help. We provide electronic data exchange and data management solutions to meet your business needs.</p>
  <div class="contact-form">
    <div class="field">Name</div><div class="field">Phone</div><div class="field">Email</div>
    <div class="field message">Message</div>
  </div>
  <div class="send" style="display:inline-block">SEND</div>
</section>

<section class="photo-band photo-map" role="img" aria-label="World map with glowing network connections and a hand touching a screen"></section>

<section class="blog">
  <h2 class="section-title"><i></i>Our Blog</h2>
  <div class="blog-row">
    <svg class="slider-arrow prev" viewBox="0 0 18 30"><path d="M15 2L3 15l12 13" fill="none" stroke="#bbb" stroke-width="3"/></svg>
    <article class="blog-card">
      <div class="blog-image" role="img" aria-label="Blue financial bar chart"></div>
      <div class="blog-content"><h3>Lorem ipsum dolor sit amet, consectetur</h3><time>October 10, 2017</time><p>Lorem ipsum dolor sit amet, consectetur adipiscing elit, sed do eiusmod tempor incididunt ut labore.</p><a>Read more »</a></div>
    </article>
    <article class="blog-card">
      <div class="blog-image" role="img" aria-label="Industrial pipes and valves"></div>
      <div class="blog-content"><h3>Lorem ipsum dolor sit amet, consectetur</h3><time>October 10, 2017</time><p>Lorem ipsum dolor sit amet, consectetur adipiscing elit, sed do eiusmod tempor incididunt ut labore.</p><a>Read more »</a></div>
    </article>
    <article class="blog-card">
      <div class="blog-image" role="img" aria-label="Oil rig at sunset"></div>
      <div class="blog-content"><h3>Lorem ipsum dolor sit amet, consectetur</h3><time>October 10, 2017</time><p>Lorem ipsum dolor sit amet, consectetur adipiscing elit, sed do eiusmod tempor incididunt ut labore.</p><a>Read more »</a></div>
    </article>
    <svg class="slider-arrow next" viewBox="0 0 18 30"><path d="M3 2l12 13L3 28" fill="none" stroke="#bbb" stroke-width="3"/></svg>
  </div>
</section>

<section class="newsletter">
  <svg viewBox="0 0 30 30"><rect x="3" y="7" width="24" height="16" fill="none" stroke="#fff" stroke-width="2"/><path d="M3 7l12 9 12-9" fill="none" stroke="#fff" stroke-width="2"/></svg>
  <h2>News letter Signup</h2>
  <div class="field">Enter Your Email</div>
  <div class="subscribe">SUBSCRIBE</div>
</section>

<footer class="site-footer">
  <div class="footer-brand">
    <div class="brand"><span class="brand-mark"></span><span class="brand-name">QOLVAR ENERGY</span></div>
    <p>Lorem ipsum dolor sit amet, consectetur adipiscing elit, sed do eiusmod tempor.</p>
  </div>
  <div class="footer-col">
    <h4>CONTACT US</h4>
    <div class="item"><svg viewBox="0 0 16 16"><path d="M8 1a5 5 0 015 5c0 4-5 9-5 9S3 10 3 6a5 5 0 015-5z" fill="#ccc"/><circle cx="8" cy="6" r="2" fill="#0b0b0b"/></svg><span>Qolvar Energy<br>410 Mesa Ridge Dr.<br>Suite 200<br>Austin, TX 78701</span></div>
    <div class="item"><svg viewBox="0 0 16 16"><path d="M4 2l3 3-2 2c1 2 2 3 4 4l2-2 3 3-2 2C7 14 2 9 2 4z" fill="#ccc"/></svg><span>806-555-0187</span></div>
    <div class="item"><svg viewBox="0 0 16 16"><rect x="1" y="3" width="14" height="10" fill="none" stroke="#ccc" stroke-width="1.5"/><path d="M1 3l7 6 7-6" fill="none" stroke="#ccc" stroke-width="1.5"/></svg><span>support@qolvarenergy.com</span></div>
  </div>
  <div class="footer-col">
    <h4>ABOUT</h4>
    <div>What We Do</div><div>Exchange Solutions</div><div>Data Management</div><div>Owner Relations Services</div><div>About QVR</div><div>Blog</div>
  </div>
  <div class="footer-col">
    <h4>GET IN TOUCH</h4>
    <div class="touch-form">
      <div class="field">Name</div><div class="field">Phone</div>
      <div class="field full">Email address</div>
      <div class="send">SEND</div>
    </div>
  </div>
</footer>
<div class="copyright">Copyright © 2017 Qolvar Energy. Electronic exchange solutions for the energy industry. All Rights Reserved.</div>

</body>
</html>
```